We need a new menu with more professional outlook for our restaurant called Bo Tien Golden Vegetarian Cuisine. We are vegetarian restaurant offered healthy food with nice environment and service. Our restaurant's pictures and take away menu are available on www.botien-eatery.example.au. I want to redesign our eat in and take away menu to be similar to our restaurant's theme and something which is green, healthy and professional. I gave the menu of my favorite restaurant on Google Docs.
Dear all,
Industry/Entity Type
Environment
Requirements
Must have
- I am really interested in the design and layout of the restaurant in our local area- please refer to these files: https://files.example.net/open?id=7K-QwertyZpLmNbVcXzAsDfGhJkLq and https://files.example.net/open?id=7K-QwertyZpLmRtYuIoPaSdFgHjKw . We would like something look like this: simple, easy to follow and professional.

```html
<!DOCTYPE html>
<html lang="en">
<head>
<meta charset="utf-8">
<title>Bo Tien Golden Vegetarian Cuisine – Take-out Menu</title>
<link rel="stylesheet" href="https://fonts.googleapis.com/css2?family=Cinzel:wght@600&family=Arimo:ital,wght@0,400;0,700;1,400&display=swap">
<style>
:root{
  --bg:#3b3b3d;
  --panel:#ffffff;
  --heading:#b3ad16;
  --ink:#1f1f1f;
  --price:#b3261e;
  --note:#9a5a32;
  --green:#8dc63f;
  --green-dark:#6a9a2a;
  --muted:#555555;
}
*{box-sizing:border-box;margin:0;padding:0}
html,body{width:848px;height:1200px;overflow:hidden;background:var(--bg)}
.canvas{position:relative;width:848px;height:1200px;background:var(--bg);font-family:"Arimo",Arial,sans-serif;color:var(--ink)}
.panel{position:absolute;background:var(--panel);padding:6px 9px;overflow:hidden}
.panel-fish{left:10px;top:6px;width:278px;height:582px}
.panel-drinks{left:299px;top:6px;width:276px;height:582px}
.panel-cover{left:584px;top:6px;width:256px;height:582px;padding:0}
.panel-starters{left:10px;top:600px;width:278px;height:594px}
.panel-noodles{left:299px;top:600px;width:276px;height:594px}
.panel-chef{left:584px;top:600px;width:256px;height:594px}

.section-title{font-family:"Cinzel",Georgia,serif;font-weight:600;color:var(--heading);font-size:14px;text-align:center;line-height:1;margin:3px 0 3px;letter-spacing:.3px}
.section-title small{display:block;font-family:"Arimo",Arial,sans-serif;font-size:5.5px;color:var(--green-dark);letter-spacing:0;margin-top:1px}

.dish-list{list-style:none}
.dish{display:flex;flex-wrap:wrap;align-items:baseline;font-size:6.2px;line-height:1.22;padding-left:6px;position:relative}
.dish::before{content:"•";position:absolute;left:0;top:0;font-size:6px}
.dish b{flex:1;font-weight:700}
.dish b i{font-weight:400;font-style:normal}
.dish em{font-style:normal;color:var(--price);font-weight:700;white-space:nowrap;margin-left:4px}
.dish small{flex-basis:100%;font-size:4.7px;line-height:1.15;color:var(--note);margin-bottom:1px}
.dish-list.airy .dish{line-height:1.45}

.byo{font-size:6px;color:var(--green-dark);font-weight:700;line-height:1.3;margin:2px 0 2px 6px}

.dessert-block{position:relative}
.dessert-block .dish b{padding-right:62px}
.dessert-photo{position:absolute;right:30px;top:2px;bottom:2px;width:56px;border-radius:4px;background:radial-gradient(circle at 50% 45%,#f0e6cf 0,#c9a16a 45%,#6b4a2e 100%)}

.extras{font-size:5.8px;color:var(--green-dark);font-weight:700;margin:2px 0 0 6px;line-height:1.35}
.extras-row{display:flex;justify-content:space-between;font-size:5.6px;color:var(--note);margin-left:10px;line-height:1.35}
.extras-row em{font-style:normal;color:var(--price);font-weight:700}

.banquet{display:grid;grid-template-columns:1fr 1fr;gap:2px 8px;font-size:5.8px;line-height:1.35;margin-left:4px}
.banquet p{font-weight:700}
.banquet .banquet-price{color:var(--price)}
.banquet .right{text-align:right}

.cover-brand{height:262px;display:flex;flex-direction:column;align-items:center;justify-content:center;gap:10px;padding:0 20px}
.brand-mark{width:58px;height:58px;border-radius:50%;background:var(--green)}
.brand-name{font-family:"Cinzel",Georgia,serif;font-weight:600;font-size:17px;color:var(--green-dark);text-align:center;line-height:1.25}
.cover-title{font-family:"Cinzel",Georgia,serif;font-weight:600;color:#3a3a3a;text-align:right;padding-right:18px;font-size:22px;line-height:1.05}
.cover-title span{display:block}
.feature-tags{display:grid;grid-template-columns:repeat(3,1fr);gap:4px;margin:12px 8px 0}
.feature-tags li{list-style:none;background:var(--green);color:#fff;font-size:7px;font-weight:700;text-align:center;padding:6px 2px;white-space:nowrap}
.cover-text{font-size:6.4px;line-height:1.4;color:var(--muted);margin:12px 10px 0}
.cover-text .gf{color:var(--green-dark);text-align:center;display:block}
.cover-contact{display:grid;grid-template-columns:1fr 1fr;gap:6px;margin:12px 10px 0;font-size:6.4px;line-height:1.35;color:var(--muted)}
.cover-contact h3{font-size:6.8px;font-weight:400;color:var(--green-dark);margin-bottom:1px}
.cover-contact .address{margin-top:5px}
.cover-contact .hours{text-align:center}
.cover-contact .closed{color:var(--green-dark);margin-top:6px}

.photo-strip{position:absolute;left:0;right:0;bottom:0;height:106px;display:flex}
.photo{position:relative;flex:1;height:100%}
.photo span{position:absolute;left:4px;bottom:8px;font-size:7px;color:#fff;text-shadow:0 0 2px #000}
.photo-a{background:linear-gradient(160deg,#d8c9a8,#8a6d46 60%,#3c2f22)}
.photo-b{background:linear-gradient(160deg,#e7d8a2,#9fb35c 55%,#4f5a2c)}
.photo-c{background:linear-gradient(160deg,#efe3c6,#b88b50 55%,#5a3d22)}
.photo-d{background:linear-gradient(160deg,#f0d08c,#c9732e 55%,#6b2f16)}
.photo-e{background:linear-gradient(160deg,#e0b070,#9a4a22 55%,#3e1c10)}
</style>
</head>
<body>
<main class="canvas">

<section class="panel panel-fish">
  <h2 class="section-title">Soy Fish</h2>
  <ul class="dish-list">
    <li class="dish"><b>FRIED SOY FISH WITH SAVOURY GINGER SAUCE – <i>Ca Gung</i></b><em>$ 15.90</em><small>Crispy soy fish tossed with fresh ginger and shallots</small></li>
    <li class="dish"><b>SOY FISH IN CLAY POT SENSATION – <i>Ca Kho To</i></b><em>$ 15.90</em><small>Braised soy fish with pepper and spring onion in clay pot</small></li>
    <li class="dish"><b>FRIED SOY FISH WITH LEMONGRASS – <i>Ca Chien Xa Ot</i></b><em>$ 15.90</em><small>Soy fish fried with onion, chilli and lemongrass flavour</small></li>
    <li class="dish"><b>SAVOURY SWEET &amp; SOUR SOY FISH – <i>Ca Xot Chua Ngot</i></b><em>$ 15.90</em><small>Tomato and onion sauce with pineapple and cucumber</small></li>
    <li class="dish"><b>SOY FISH WITH TAMARIND SAUCE – <i>Ca Xot Me</i></b><em>$ 16.90</em></li>
  </ul>
  <h2 class="section-title">Soy Chicken</h2>
  <ul class="dish-list">
    <li class="dish"><b>HONEY ROAST SOY CHICKEN – <i>Ga Mat Ong</i></b><em>$ 15.90</em><small>Crispy soy chicken drizzled in honey sauce</small></li>
    <li class="dish"><b>SOY CHICKEN AND CASHEW NUT – <i>Ga Hot Dieu</i></b><em>$ 16.90</em><small>A mixture of fresh vegetables tossed in a light sauce and cashew nuts</small></li>
    <li class="dish"><b>LEMON GRASS SOY CHICKEN (SPICY) – <i>Ga Xa Ot (Cay)</i></b><em>$ 15.90</em><small>Minced lemongrass and chilli with soy chicken and onions</small></li>
    <li class="dish"><b>GINGER SOY CHICKEN – <i>Ga Gung</i></b><em>$ 15.90</em><small>Thin ginger strips stir fried with soy chicken and capsicum</small></li>
    <li class="dish"><b>SOY CHICKEN CURRY &amp; VEGGIE WITH COCONUT CREAM – <i>Ca Ri Chay</i></b><em>$ 15.90</em><small>Coconut cream curry with potato, carrot and vegetables</small></li>
    <li class="dish"><b>SOY CHICKEN WITH BASIL LEAVE – <i>Ga La Que</i></b><em>$ 15.90</em><small>A combination of capsicum, basil and onion in soy sauce</small></li>
    <li class="dish"><b>SOY CHICKEN SATAY SAUCE (SPICY) – <i>Ga Xao Sate (Cay)</i></b><em>$ 15.90</em><small>Authentic satay with vegetables, carrots and broccoli</small></li>
    <li class="dish"><b>LEMON SOY CHICKEN – <i>Ga Chanh</i></b><em>$ 15.90</em><small>Crispy soy chicken in lemon sauce</small></li>
    <li class="dish"><b>SOY CHICKEN ON HOT PLATE – <i>Ga Vi Sat</i></b><em>$ 15.90</em><small>Sizzling soy chicken with capsicum, celery and onions</small></li>
    <li class="dish"><b>SHANTON CHICKEN – <i>Ga Shanton</i></b><em>$ 15.90</em><small>Crispy soy chicken in Shanton sauce</small></li>
    <li class="dish"><b>SOY CHICKEN DRUMSTICK AND BOK CHOY IN SOY SAUCE – <i>Dui Ga Xa Xiu</i></b><em>$ 15.90</em><small>Soy chicken drumstick with steamed bok choy</small></li>
    <li class="dish"><b>CHICKEN IN PLUM SAUCE – <i>Ga Xi Muoi</i></b><em>$ 15.90</em></li>
  </ul>
  <h2 class="section-title">Tofu Delight</h2>
  <ul class="dish-list">
    <li class="dish"><b>BRAISED TOFU AND VEGETABLE – <i>Dau Hu Xao Rau</i></b><em>$ 14.90</em><small>Fresh vegetables with tofu tossed in our special sauce</small></li>
    <li class="dish"><b>STUFFED BEANCURD IN DELIGHT SWEET &amp; SOUR SAUCE – <i>Dau Hu Don</i></b><em>$ 15.90</em><small>Tomato and lemon sauce with pineapple and cucumbers</small></li>
    <li class="dish"><b>TOFU WITH LEMON GRASS (SPICY) – <i>Dau Hu Xao Xa Ot</i></b><em>$ 14.90</em><small>A combination of tofu with lemongrass and chilli</small></li>
    <li class="dish"><b>TOFU WITH SATAY SAUCE (SPICY) – <i>Dau Hu Xao Satay</i></b><em>$ 14.90</em><small>Authentic satay with cauliflower, carrots and broccoli</small></li>
    <li class="dish"><b>BRAISED TOFU AND VEGETABLE WITH CASHEW NUT – <i>Dau Hu Xao Hat Dieu</i></b><em>$ 15.90</em><small>A mixture of fresh vegetables tossed in a light sauce</small></li>
  </ul>
  <h2 class="section-title">Rice</h2>
  <ul class="dish-list airy">
    <li class="dish"><b>RICE &amp; VEGGIE COMBINATION – <i>Com Xao Rau Cai</i></b><em>$ 12.00</em></li>
    <li class="dish"><b>RICE &amp; SATAY TOFU – <i>Com Dau Hu Sate</i></b><em>$ 12.00</em></li>
    <li class="dish"><b>RICE &amp; SOY TUNA IN TOMATO SAUCE – <i>Com Tuna Sot Ca Chua</i></b><em>$ 12.00</em></li>
    <li class="dish"><b>SMALL COMBINATION FRIED RICE – <i>Com Chien Thap Cam Nho</i></b><em>$ 6.90</em></li>
    <li class="dish"><b>LARGE COMBINATION FRIED RICE – <i>Com Chien Thap Cam Lon</i></b><em>$ 7.90</em></li>
    <li class="dish"><b>STEAMED RICE (PER PERSON) – <i>Com Trang (Mot Nguoi)</i></b><em>$ 2.50</em></li>
  </ul>
</section>

<section class="panel panel-drinks">
  <h2 class="section-title">Beverages</h2>
  <ul class="dish-list airy">
    <li class="dish"><b>MIXED LOTUS, SEAWEED (GLASS) – <i>Sam Bo Luong</i></b><em>$ 4.90</em><small>Served with blended ice</small></li>
    <li class="dish"><b>THREE COLOURED BEAN DRINK (GLASS) – <i>Che Ba Mau</i></b><em>$ 4.90</em><small>Served with blended ice</small></li>
    <li class="dish"><b>FRESH ORANGE JUICE (GLASS)</b><em>$ 4.90</em><small>Freshly squeezed</small></li>
    <li class="dish"><b>YOUNG COCONUT JUICE (GLASS) – <i>Nuoc Dua Tuoi</i></b><em>$ 3.90</em></li>
    <li class="dish"><b>SOY BEAN DRINK (GLASS) (HOT OR COLD) – <i>Sua Dau Nanh</i></b><em>$ 3.90</em><small>Homemade soybean drink</small></li>
    <li class="dish"><b>LEMON ICE TEA (GLASS) – <i>Tra Da Chanh</i></b><em>$ 3.90</em></li>
    <li class="dish"><b>VIETNAMESE ICE COFFEE (GLASS) – <i>Ca Phe Sua Da</i></b><em>$ 3.90</em></li>
    <li class="dish"><b>JASMINE OR GREEN HOT TEA (PER PERSON) – <i>Tra Nong</i></b><em>$ 1.80</em></li>
    <li class="dish"><b>LEMON LIME BITTERS (GLASS)</b><em>$ 3.90</em></li>
    <li class="dish"><b>LEMON SODA WATER (GLASS)</b><em>$ 3.90</em></li>
    <li class="dish"><b>APPLE JUICE (GLASS)</b><em>$ 3.90</em></li>
    <li class="dish"><b>ALOE VERA JUICE (GLASS)</b><em>$ 3.90</em></li>
    <li class="dish"><b>SOFT DRINK (CAN)</b><em>$ 3.20</em></li>
  </ul>
  <p class="byo">Includes: COLA, DIET COLA, ZERO COLA, LEMONADE, ORANGE SODA, LEMON SODA<br>WE ARE WELCOME BYO $ 1.00 CHARGED PER CORKAGE</p>
  <h2 class="section-title">Desserts</h2>
  <div class="dessert-block">
    <ul class="dish-list airy">
      <li class="dish"><b>FRESH YOUNG COCONUT JELLY</b><em>$ 4.90</em></li>
      <li class="dish"><b>DEEP FRIED ICE CREAM</b><em>$ 6.90</em></li>
      <li class="dish"><b>DEEP FRIED SOY ICE CREAM</b><em>$ 6.90</em></li>
      <li class="dish"><b>BANANA CAKE &amp; COCONUT CREAM OR ICE CREAM</b><em>$ 6.90</em></li>
      <li class="dish"><b>BANANA FRITTER &amp; COCONUT CREAM OR ICE CREAM</b><em>$ 6.90</em></li>
      <li class="dish"><b>CARAMEL FLAN (NO EGG) &amp; ICE CREAM</b><em>$ 4.90</em></li>
      <li class="dish"><b>LYCEE &amp; ICE CREAM</b><em>$ 4.90</em></li>
      <li class="dish"><b>LOGAN &amp; ICE CREAM</b><em>$ 4.90</em></li>
      <li class="dish"><b>SUNDAE ICE CREAM</b><em>$ 4.00</em></li>
    </ul>
    <div class="dessert-photo" role="img" aria-label="Photo of a plated dessert with ice cream"></div>
  </div>
  <p class="extras">+ EXTRAS:</p>
  <p class="extras-row">TOPPING WITH CHOCOLATE, CARAMEL OR STRAWBERRY <em>$ 0.50</em></p>
  <p class="extras-row">TOPPING WITH PEANUTS <span>OPTIONAL</span></p>
  <p class="extras-row">SOY ICE CREAM ALTERNATIVES AVAILABLE ON REQUEST</p>
  <h2 class="section-title">Banquet</h2>
  <div class="banquet">
    <div>
      <p class="banquet-price">$25.00 PER PERSON (Minimum 4 persons)</p>
      <p>*SPRING ROLLS</p><p>*ROAST SOY DUCK WRAP</p><p>*FRESH COLD ROLLS</p><p>*SIZZLING MONGOLIAN SOY LAMB</p><p>*HONEY SOY CHICKEN</p><p>*BUDDHA'S FEAST</p><p>*COMBINATION FRIED AND STEAMED RICE</p><p>*FOUR SEASON FRUITS</p>
    </div>
    <div class="right">
      <p class="banquet-price">$27.00 PER PERSON (Minimum 4 persons)</p>
      <p>*SPRING ROLLS</p><p>*SOY CHICKEN SATAY STICKS</p><p>*CURRY PUFFS</p><p>*FRESH COLD ROLLS</p><p>*SIZZLING MONGOLIAN SOY LAMB</p><p>*BRAISED TOFU AND VEGETABLES WITH CASHEW NUTS</p><p>*EGG PLANT IN CLAY POT</p><p>*COMBINATION FRIED RICE AND STEAMED RICE</p><p>*FOUR SEASON FRUITS</p>
    </div>
  </div>
</section>

<section class="panel panel-cover">
  <div class="cover-brand">
    <span class="brand-mark" aria-hidden="true"></span>
    <p class="brand-name">Bo Tien Golden Vegetarian Cuisine</p>
  </div>
  <h1 class="cover-title"><span>Take - out</span><span>Menu</span></h1>
  <ul class="feature-tags">
    <li>NO EGG</li><li>NO MSG</li><li>NO CHOLESTEROL</li>
    <li>HEALTHY/ LOW FAT</li><li>TASTY</li>
  </ul>
  <p class="cover-text">All our dishes are vegetarian and prepared fresh without eggs, wine or MSG. All vegetarian imitation "meat" dishes like beef, pork, chicken, duck, fish, squid and seafood are made out of SOYBEAN proteins. We only use Vegetable oil in our cooking.<span class="gf">** Gluten Free or Nut Free are available on request**</span></p>
  <div class="cover-contact">
    <div>
      <h3>Contact information</h3>
      <p>T: 02 5550 4817<br>F: 02 5550 4818</p>
      <h3 class="address">Address:</h3>
      <p>Shop 7/12 Fernvale Street<br>HARTWELL, ACT<br>Australia 2609</p>
    </div>
    <div class="hours">
      <h3>Opening hours :</h3>
      <p>Tuesday- Sunday lunch<br>11:30am- 2:30 pm<br>Monday- Sunday dinner<br>5:30pm- 10:30 pm</p>
      <p class="closed">CLOSED CHRISTMAS</p>
    </div>
  </div>
</section>

<section class="panel panel-starters">
  <h2 class="section-title">Appetizers</h2>
  <ul class="dish-list">
    <li class="dish"><b>BO TIEN SPRING ROLLS (4 ROLLS) – <i>Cha Gio Bo Tien</i></b><em>$ 6.90</em></li>
    <li class="dish"><b>VEGETARIAN SPRING ROLLS (4 ROLLS) – <i>Cha Gio</i></b><em>$ 6.90</em></li>
    <li class="dish"><b>SHREDDED TOFU ROLLS (2 ROLLS) – <i>Bi Cuon</i></b><em>$ 5.50</em></li>
    <li class="dish"><b>FRESH COLD ROLLS (2 ROLLS) – <i>Goi Cuon</i></b><em>$ 5.50</em></li>
    <li class="dish"><b>POCKET MONEY BAGS (6 PIECES) – <i>Tui Tien</i></b><em>$ 6.90</em></li>
    <li class="dish"><b>DEEP-FRIED WONTON (5 PIECES) – <i>Hoanh Thanh Chien</i></b><em>$ 6.90</em></li>
    <li class="dish"><b>SOY CHICKEN NUGGETS (8 PIECES) – <i>Ga Chien</i></b><em>$ 6.90</em></li>
    <li class="dish"><b>SOY CHICKEN DRUMSTICKS (5 PIECES) – <i>Dui Ga</i></b><em>$ 6.90</em></li>
    <li class="dish"><b>SOY CHICKEN SATAY STICKS (6 STICKS) – <i>Ga Lui</i></b><em>$ 6.90</em></li>
    <li class="dish"><b>MUSHROOM FRITTERS (5 PIECES) – <i>Nam Lan Bot</i></b><em>$ 6.90</em></li>
    <li class="dish"><b>EGGPLANT FRITTERS – <i>Ca Tim Lan Bot</i></b><em>$ 6.90</em></li>
    <li class="dish"><b>DEEP-FRIED TOFU – <i>Dau Hu Chien Don</i></b><em>$ 6.90</em></li>
    <li class="dish"><b>SOY CRABMEAT PATE – <i>Cha Cua</i></b><em>$ 6.90</em></li>
    <li class="dish"><b>B.B.Q SOY MEAT SKEWER – <i>Thit Nuong</i></b><em>$ 8.00</em></li>
    <li class="dish"><b>CURRY PUFF (4 PIECES) – <i>Banh Cari</i></b><em>$ 6.90</em></li>
    <li class="dish"><b>SOY SHRIMP ON TOAST (4 PIECES) – <i>Banh Mi Chien</i></b><em>$ 6.90</em></li>
    <li class="dish"><b>SOY CHICKEN SALAD – <i>Goi Ga</i></b><em>$ 11.00</em></li>
    <li class="dish"><b>BO TIEN SPECIAL SALAD – <i>Goi Sua</i></b><em>$ 11.00</em></li>
    <li class="dish"><b>PAW PAW SALAD – <i>Goi Du Du</i></b><em>$ 11.00</em></li>
    <li class="dish"><b>ASPARAGUS SOUP – <i>Sup Mang Tay</i></b><em>$ 6.90</em></li>
    <li class="dish"><b>CORN SOUP – <i>Sup Bap</i></b><em>$ 6.90</em></li>
    <li class="dish"><b>WONTON SOUP – <i>Hoanh Thanh Sup</i></b><em>$ 7.90</em></li>
    <li class="dish"><b>SOY DUCK WRAP (4 PIECES) – <i>Vit Cuon</i></b><em>$ 6.90</em></li>
    <li class="dish"><b>VEGGIE DUMPLING – <i>Banh Xep Chien</i></b><em>$ 6.90</em></li>
    <li class="dish"><b>VEGETABLE STEAMED BUNS (4 BUNS) – <i>Banh Bao</i></b><em>$ 6.90</em></li>
  </ul>
  <h2 class="section-title">Fresh Vegetables</h2>
  <ul class="dish-list">
    <li class="dish"><b>BUDDHA'S FEAST – <i>Rau Xao Thap Cam</i></b><em>$ 14.90</em><small>Freshly prepared vegetables lightly tossed in our special sauce</small></li>
    <li class="dish"><b>ASSORTED STEAMED VEGETABLE – <i>Rau Hap Thap Cam</i></b><em>$ 14.90</em><small>Freshly prepared vegetables steamed, served with mushroom sauce</small></li>
    <li class="dish"><b>CURRY VEGETABLE WITH COCONUT CREAM – <i>Rau lan chay</i></b><em>$ 14.90</em><small>Coconut cream sauce served with cauliflower and broccoli</small></li>
    <li class="dish"><b>BRAISED SNOW PEAS AND ABALONE MUSHROOM – <i>Dau Hoa Lan</i></b><em>$ 15.90</em><small>Snow peas and mushroom tossed in a light sauce</small></li>
    <li class="dish"><b>BRAISED GREEN BEAN AND SOY BEEF – <i>Bo Xao Dau Que</i></b><em>$ 15.90</em></li>
    <li class="dish"><b>BRAISED GREEN BEAN AND SOY CHICKEN – <i>Ga Xao Dau Que</i></b><em>$ 15.90</em></li>
  </ul>
  <div class="photo-strip">
    <div class="photo photo-a" role="img" aria-label="Photo of Vietnamese cannelloni"><span>Vietnamese Cannelloni</span></div>
    <div class="photo photo-b" role="img" aria-label="Photo of paw paw salad"><span>Paw Paw Salad</span></div>
  </div>
</section>

<section class="panel panel-noodles">
  <h2 class="section-title">Vietnamese Noodle Specialties<small>(Served With Or Without Onions And Shallots)</small></h2>
  <ul class="dish-list">
    <li class="dish"><b>BO TIEN SOY BEEF SOUP – <i>Pho Bo Dac Biet</i></b><em>$ 12.50</em></li>
    <li class="dish"><b>BO TIEN SOY CHICKEN SOUP – <i>Pho Ga</i></b><em>$ 12.50</em></li>
    <li class="dish"><b>SOY PORK RICE NOODLE SOUP – <i>Hu Tieu Nuoc</i></b><em>$ 12.50</em></li>
    <li class="dish"><b>SOY PORK DRY RICE NOODLE SOUP – <i>Hu Tieu Kho</i></b><em>$ 12.50</em><small>Served with separate bowl of soup and savoury sauce</small></li>
    <li class="dish"><b>SOY SEAFOOD RICE NOODLE SOUP – <i>Hu Tieu Do Bien</i></b><em>$ 13.50</em></li>
    <li class="dish"><b>SOY CHICKEN YELLOW NOODLE SOUP – <i>Mi Ga</i></b><em>$ 12.50</em></li>
    <li class="dish"><b>SOY DUCK YELLOW NOODLE SOUP – <i>Mi Vit</i></b><em>$ 13.50</em></li>
    <li class="dish"><b>WONTON YELLOW NOODLE SOUP – <i>Hoanh Thanh Mi</i></b><em>$ 12.50</em></li>
    <li class="dish"><b>COMBINATION LAKSA NOODLE – <i>Mi Lac Xa</i></b><em>$ 13.50</em></li>
    <li class="dish"><b>ROYAL SPICY NOODLE SOUP – <i>Bun Bo Hue (Cay)</i></b><em>$ 12.50</em></li>
    <li class="dish"><b>THICK STARCH HOME MADE NOODLE SOUP – <i>Banh Canh</i></b><em>$ 12.50</em></li>
    <li class="dish"><b>RICE VERMICELLI WITH SPRING ROLLS – <i>Bun Cha Gio</i></b><em>$ 12.50</em></li>
    <li class="dish"><b>RICE VERMICELLI SPRING ROLLS &amp; TOFU – <i>Bun Bi Cha Gio</i></b><em>$ 12.50</em></li>
    <li class="dish"><b>RICE VERMICELLI WITH B.B.Q SOY MEAT – <i>Bun Thit Nuong</i></b><em>$ 12.50</em></li>
    <li class="dish"><b>COMBINATION SOY MEAT VEGGIE STIR FRY RICE NOODLE – <i>Hu Tieu Xao</i></b><em>$ 17.00</em></li>
    <li class="dish"><b>COMBINATION SOY SEAFOOD VEGGIE STIR FRY RICE NOODLE</b><em>$ 18.00</em><small>Hu Tieu Xao Do Bien Thap Cam</small></li>
    <li class="dish"><b>COMBINATION SOY MEAT VEGGIE SOFT OR CRISPY NOODLE – <i>Mi Xao</i></b><em>$ 17.00</em></li>
    <li class="dish"><b>COMBINATION SOY SEAFOOD VEGGIE SOFT OR CRISPY NOODLE</b><em>$ 18.00</em><small>Mi Xao Do Bien Mem / Don</small></li>
  </ul>
  <h2 class="section-title">Soy Beef</h2>
  <ul class="dish-list">
    <li class="dish"><b>SOY BEEF CURRY &amp; VEGGIE WITH COCONUT CREAM – <i>Bo Ca Ri</i></b><em>$ 15.90</em><small>Coconut cream sauce with cauliflower, carrots and celery</small></li>
    <li class="dish"><b>SOY BEEF SATAY SAUCE (SPICY) – <i>Bo Xao Sate</i></b><em>$ 15.90</em><small>Authentic satay sauce with cauliflower, carrots and broccoli</small></li>
    <li class="dish"><b>SOY BEEF AND PEANUT – <i>Bo Dau Phong</i></b><em>$ 15.90</em><small>Onions, capsicum and salad stirred in a light sauce</small></li>
    <li class="dish"><b>SOY BEEF AND CASHEW NUT – <i>Bo Hot Dieu</i></b><em>$ 16.90</em><small>Fresh vegetables and soy beef tossed in a light sauce</small></li>
    <li class="dish"><b>SOY BEEF ON HOT PLATE – <i>Bo Vi Sat</i></b><em>$ 15.90</em><small>Sizzling soy beef with capsicum, celery and onions</small></li>
    <li class="dish"><b>SOY BEEF GINGER – <i>Bo Gung</i></b><em>$ 15.90</em><small>Thin ginger strips stir fried with soy beef</small></li>
    <li class="dish"><b>SOY BEEF RENDANG – <i>Bo Rendang</i></b><em>$ 15.90</em><small>Authentic rendang sauce with onions and cucumbers</small></li>
  </ul>
  <div class="photo-strip">
    <div class="photo photo-c" role="img" aria-label="Photo of soy pork dry noodle soup"><span>Soy Pork Dry Noodle Soup</span></div>
    <div class="photo photo-d" role="img" aria-label="Photo of house sweet and sour soup"><span>Bo Tien Sweet and Sour Soup</span></div>
    <div class="photo photo-e" role="img" aria-label="Photo of roast soy duck"><span>Roast Soy Duck</span></div>
  </div>
</section>

<section class="panel panel-chef">
  <h2 class="section-title">Chef's Special</h2>
  <ul class="dish-list">
    <li class="dish"><b>VIETNAMESE CANNELLONI – <i>Banh Cuon</i></b><em>$ 13.90</em><small>Homemade rice paper roll with soy meat and mushroom, served with sauce</small></li>
    <li class="dish"><b>VIETNAMESE CREPE – <i>Banh Xeo</i></b><em>$ 15.90</em><small>Crispy crepe with tofu, vegetable, bean and soy ham, served with salad</small></li>
    <li class="dish"><b>VIETNAMESE RICE VERMICELLI CAKE AND B.B.Q SOY MEAT</b><em>$ 16.90</em><small>Banh Hoi Thit Nuong, served with fresh salad</small></li>
    <li class="dish"><b>BO TIEN BROKEN RICE – <i>Com Tam Bi Suon Cha</i></b><em>$ 14.90</em><small>Broken rice with B.B.Q soy meat, shredded tofu and soup</small></li>
    <li class="dish"><b>SPECIAL STEW SOY BEEF – <i>Bo Kho</i></b><em>$ 15.90</em></li>
    <li class="dish"><b>SMALL BO TIEN SWEET AND SOUR SOUP – <i>Canh Chua Nho</i></b><em>$ 15.90</em><small>Banana flower, pineapple, tomato and bean sprouts</small></li>
    <li class="dish"><b>LARGE BO TIEN SWEET AND SOUR SOUP – <i>Canh Chua Lon</i></b><em>$ 17.90</em><small>Banana flower, pineapple, tomato and bean sprouts</small></li>
    <li class="dish"><b>SMALL SOY SEAFOOD SWEET AND SOUR SOUP</b><em>$ 16.90</em><small>Canh Chua Do Bien Nho, with tomato and celery</small></li>
    <li class="dish"><b>LARGE SOY SEAFOOD SWEET AND SOUR SOUP</b><em>$ 18.90</em><small>Canh Chua Do Bien Lon, with tomato and celery</small></li>
    <li class="dish"><b>SMALL SOY BEEF SWEET &amp; SOUR SOUP (SPICY)</b><em>$ 15.90</em><small>Canh Chua Thit Bo Nho (Cay)</small></li>
    <li class="dish"><b>LARGE SOY BEEF SWEET &amp; SOUR SOUP (SPICY)</b><em>$ 17.90</em><small>Canh Chua Thit Bo Lon (Cay)</small></li>
    <li class="dish"><b>SMALL STUFFED BITTER MELON SOUP – <i>Canh Kho Qua Nho</i></b><em>$ 14.90</em></li>
    <li class="dish"><b>LARGE STUFFED BITTER MELON SOUP – <i>Canh Kho Qua Lon</i></b><em>$ 16.90</em></li>
    <li class="dish"><b>SWEET &amp; SOUR SOY SQUID – <i>Muc Chua Ngot</i></b><em>$ 15.90</em><small>Tomato and lemon sauce with pineapple and onions</small></li>
    <li class="dish"><b>CHILLI SOY SQUID WITH VARIETY VEGETABLE – <i>Muc Xao Rau</i></b><em>$ 15.90</em><small>Fresh vegetables and soy squid in our special sauce</small></li>
    <li class="dish"><b>FRIED SOY SQUID WITH SPICY SALT &amp; CHILLI</b><em>$ 16.90</em><small>Muc Chien Muoi Ot, served with chilli and onions</small></li>
    <li class="dish"><b>FRIED CRAB WITH SPICY SALT &amp; CHILLI – <i>Cua Muoi</i></b><em>$ 16.90</em><small>Soy crab with salt, chilli and onions</small></li>
    <li class="dish"><b>EGGPLANT IN CLAYPOT SENSATION – <i>Ca Tim</i></b><em>$ 15.90</em><small>Mushroom and eggplant drizzled with our sauce</small></li>
    <li class="dish"><b>ROAST SOY DUCK – <i>Vit Quay</i></b><em>$ 15.90</em></li>
    <li class="dish"><b>SOY DUCK IN PLUM SAUCE – <i>Vit Xi Muoi</i></b><em>$ 15.90</em></li>
    <li class="dish"><b>ROAST SOY PORK – <i>Xa Xiu</i></b><em>$ 15.90</em></li>
    <li class="dish"><b>MONGOLIAN SOY LAMB – <i>Truu Nuong Mong Co</i></b><em>$ 15.90</em></li>
    <li class="dish"><b>BO TIEN EIGHT TREASURE – <i>Bat Buu</i></b><em>$ 16.90</em><small>All special soy meat, tofu and vegetables stir fry</small></li>
    <li class="dish"><b>GRILLED SOY FISH SENSATION – <i>Ca Nuong Trui</i></b><em>$ 40.00</em><small>Served with rice paper, salad and savoury sauce</small></li>
    <li class="dish"><b>SMALL VIETNAMESE FONDUE – <i>Lau Thap Cam Nho</i></b><em>$ 45.00</em><small>Clear soup served with soy meats and vermicelli</small></li>
    <li class="dish"><b>LARGE VIETNAMESE FONDUE – <i>Lau Thap Cam Lon</i></b><em>$ 60.00</em><small>Clear soup served with soy meats and vermicelli</small></li>
  </ul>
</section>

</main>
</body>
</html>
```